Client Fulfillment Flyer

This is a document used for internal purposes ie it is not distributed to clients. We would like it to have some colour, images etc. We are in the financial services industry, Ballarat, Victoria, Australia. www.tarrowfield.com.au and www.tarrowfieldagri.com.au

Target Market(s)

Internal training document

Industry/Entity Type

Finance And Accounting

Colors
3176b5

```html
<!DOCTYPE html>
<html lang="en">
<head>
<meta charset="utf-8">
<title>Tarrowfield &amp; Co – Client Fulfillment</title>
<link href="https://fonts.googleapis.com/css2?family=Source+Sans+3:ital,wght@0,400;0,600;1,400&display=swap" rel="stylesheet">
<style>
  :root {
    --brand-blue: #1a5fd8;
    --band-dark: #02095a;
    --band-mid: #0a2fa8;
    --band-light: #1f6ae8;
    --text: #4b5056;
    --rule: #e1e3e6;
    --paper: #ffffff;
  }
  html, body {
    margin: 0;
    padding: 0;
    overflow: hidden;
    background: var(--paper);
  }
  .page {
    position: relative;
    width: 939px;
    height: 1200px;
    overflow: hidden;
    background: var(--paper);
    font-family: "Source Sans 3", "Source Sans Pro", sans-serif;
    color: var(--text);
  }
  .rule {
    position: absolute;
    left: 77px;
    width: 793px;
    height: 1px;
    background: var(--rule);
  }
  .rule--top { top: 76px; }
  .rule--bottom { top: 1126px; }
  .header-band {
    position: absolute;
    left: 0;
    top: 107px;
    width: 939px;
    height: 55px;
    background: linear-gradient(90deg, var(--band-dark) 0%, var(--band-mid) 22%, var(--band-light) 50%, var(--band-mid) 78%, var(--band-dark) 100%);
  }
  .brand-dot {
    position: absolute;
    left: 436px;
    top: 100px;
    width: 68px;
    height: 68px;
    border-radius: 50%;
    background: var(--paper);
  }
  .brand-name {
    position: absolute;
    left: 0;
    width: 939px;
    top: 171px;
    text-align: center;
    font-size: 21px;
    font-weight: 600;
    letter-spacing: 1px;
    color: var(--brand-blue);
    margin: 0;
  }
  .content {
    position: absolute;
    left: 142px;
    width: 656px;
    top: 0;
  }
  .section-title {
    position: absolute;
    left: 0;
    margin: 0;
    font-size: 17.6px;
    font-weight: 400;
    letter-spacing: 0.3px;
    color: var(--brand-blue);
  }
  .body-text {
    position: absolute;
    left: 0;
    width: 656px;
    margin: 0;
    font-size: 13.6px;
    line-height: 20.2px;
    text-align: justify;
  }
  .focus-list {
    position: absolute;
    left: 0;
    top: 552px;
    margin: 0;
    padding: 0;
    list-style: none;
    font-size: 13.6px;
    line-height: 20.2px;
  }
  .focus-list li {
    position: relative;
    padding-left: 53px;
  }
  .focus-list li::before {
    content: "•";
    position: absolute;
    left: 0;
    font-size: 10px;
  }
  .vision-intro {
    position: absolute;
    left: 0;
    top: 876px;
    margin: 0;
    font-size: 13.6px;
    font-style: italic;
  }
  .vision-statement {
    position: absolute;
    left: -142px;
    width: 939px;
    top: 917px;
    margin: 0;
    text-align: center;
    font-size: 13.6px;
    line-height: 20.2px;
  }
  .page-number {
    position: absolute;
    left: 446px;
    top: 1101px;
    width: 48px;
    height: 48px;
    border-radius: 50%;
    background: var(--paper);
    box-shadow: 0 -1px 2px rgba(0,0,0,0.12);
  }
  .page-number span {
    position: absolute;
    left: 8px;
    top: 8px;
    width: 32px;
    height: 32px;
    border-radius: 50%;
    background: var(--brand-blue);
    color: #fff;
    font-size: 17px;
    line-height: 32px;
    text-align: center;
  }
</style>
</head>
<body>
<div class="page">
  <div class="rule rule--top"></div>

  <header>
    <div class="header-band"></div>
    <div class="brand-dot"></div>
    <p class="brand-name">TARROWFIELD &amp; CO</p>
  </header>

  <main class="content">
    <h2 class="section-title" style="top:286px;">Client Fulfillment</h2>
    <p class="body-text" style="top:330px;">We are primarily a service based business however the product we sell is Client Fulfillment.&nbsp; Client Fulfillment in simple terms means providing the services to satisfy client requirements and expectations.&nbsp; Our aim is to not only satisfy but exceed client requirements and expectations.The Client Fulfillment system is the methodology through which we deliver the result we have promised to deliver.Why is this important?&nbsp; In order to achieve our Core Purpose and Vision, delivering Client Fulfillment is essential.</p>

    <h2 class="section-title" style="top:469px;">The Client Fulfillment Process</h2>
    <p class="body-text" style="top:512px;">The areas we focus on to deliver Client Fulfillment are:</p>

    <ul class="focus-list">
      <li>Understanding Core Purpose, Core Values, Vision and Why</li>
      <li>Client Management and Communication</li>
      <li>The Basics</li>
      <li>The Are You Financially Secure Process</li>
      <li>The Right People Doing the Right Work</li>
    </ul>

    <p class="body-text" style="top:674px;">Understanding Core Purpose, Core Values, Vision and Why<br>These terms can be overwhelming and confusing but to deliver Client Fulfillment it is important to understand what it all means and how it all connects.<br>Our Core Purpose and Core Values are the foundation of our business. We have a clear Vision of where we want the business to go, that is what does it look like in 10 years. Underlying this is our WHY. We know what we do and how to do it, but more importantly is WHY we do it and what drives us each day to help our clients.</p>

    <h2 class="section-title" style="top:834px;">Our Vision.&nbsp; What is it?</h2>
    <p class="vision-intro">This is our Vision across the entire Tarrowfield &amp; Co business:</p>

    <p class="vision-statement">To provide all businesses and individuals with the opportunity to achieve financial security.<br>Our business is designed so people can access all the services required to achieve financial security.<br>We are a motivated team that embraces change and technology along with having the knowledge,<br>skills and expertise to help committed clients achieve financial security.<br>We believe everyone deserves this opportunity and we are committed to proactively engage with<br>existing and future clients to share and demonstrate the positive impact we can make to their lives.<br>We do not limit the number of people we can help and distance is not a barrier.</p>
  </main>

  <footer>
    <div class="rule rule--bottom"></div>
    <div class="page-number"><span>2</span></div>
  </footer>
</div>
</body>
</html>
```